4 panel (or page) brochure

We need a brochure design for a Oklahoma based company. We manufacture and sell underground and below ground shelters. We sell our shelters in our local showroom, as well distribute our shelters to a big box national retailer. I would like to have a simple design that includes a few pictures of our product and details on each product we offer as well as install details for each product. Our out of state retailers likely will not have our product display so we will need something that sells the product without seeing it in person.

I would like something that it easily printable as well as able to edit at a later time if needed.

I've included Catalog/Brochure Copy
Pictures of Below Ground Units/Above Ground Units - feel free to edit or touch up.
Some brochure ideas I found on LayoutNest that seemed to be similar to what we can do.
The Inside of a brochure we did a while back that we liked (style-wise)
A general info flyer for more information

It Company

```html
<!DOCTYPE html>
<html lang="en">
<head>
<meta charset="utf-8">
<title>StormHaven Above Ground Safe Rooms Brochure</title>
<link href="https://fonts.googleapis.com/css2?family=Raleway:wght@300;400;500;600;700;800&display=swap" rel="stylesheet">
<style>
  :root {
    --red: #d0202a;
    --red-dark: #b81a23;
    --ink: #3a3a3a;
    --grey-head: #bdbdbd;
    --grey-row: #e6e6e6;
    --grey-alt: #a9a9a9;
    --trim: #8fd08f;
    --paper: #ffffff;
    --crop: #9a9a9a;
  }
  * { box-sizing: border-box; margin: 0; padding: 0; }
  html, body { width: 1200px; height: 900px; overflow: hidden; background: var(--paper); }
  body { position: relative; font-family: "Raleway", Arial, sans-serif; color: var(--ink); }
  .abs { position: absolute; }

  .trim-box { left: 42px; top: 55px; width: 1118px; height: 793px; border: 1px solid var(--trim); }
  .fold-line { left: 600px; width: 0; border-left: 1px dashed var(--crop); }
  .crop { background: var(--crop); }

  .title-banner { left: 32px; top: 93px; width: 534px; height: 61px; }
  .title-text { left: 340px; top: 105px; color: #fff; font-size: 17px; line-height: 20px; letter-spacing: .3px; }
  .title-text strong { font-weight: 800; display: block; }
  .title-text span { font-weight: 400; display: block; padding-left: 19px; }
  .title-mark { left: 340px; top: 109px; width: 11px; height: 11px; }

  .photo { background: linear-gradient(160deg, #f4f4f4, #d9d9d9); }

  .intro { left: 401px; top: 182px; width: 166px; font-size: 7.6px; line-height: 13px; }

  .section-head { color: var(--red); font-size: 7.6px; font-weight: 700; letter-spacing: .2px; }

  table { border-collapse: collapse; font-size: 7.4px; }
  th { background: var(--grey-head); font-weight: 700; color: var(--ink); height: 12px; }
  td { height: 14px; text-align: center; }
  .sizes { left: 76px; top: 392px; width: 162px; }
  .sizes tr:nth-child(even) td { background: var(--grey-alt); color: #fff; }
  .sizes tr:nth-child(odd) td { background: var(--grey-row); }

  ul.bullets { list-style: none; font-size: 7.6px; line-height: 11.2px; }
  ul.bullets li { position: relative; padding-left: 9px; margin-bottom: 3.5px; }
  ul.bullets li::before { content: "•"; position: absolute; left: 0; }

  .custom { left: 253px; top: 660px; width: 312px; }
  .custom th { text-align: center; }
  .custom td { background: var(--grey-row); vertical-align: top; text-align: left; padding: 2px 5px; line-height: 9.5px; }
  .custom td.loc { text-align: center; padding: 0; }
  .custom td.loc div { height: 11.6px; line-height: 11.6px; }
  .custom td.loc div.alt { background: var(--grey-alt); color: #fff; }

  .brand { display: flex; align-items: center; gap: 5px; font-weight: 800; color: var(--red); letter-spacing: .4px; }
  .brand i { display: inline-block; border-radius: 50%; background: var(--red); }

  .footer-rule { left: 180px; top: 772px; width: 1px; height: 56px; background: var(--ink); }
  .visit { left: 191px; top: 771px; font-size: 8px; }
  .office { font-size: 7.4px; line-height: 9.6px; }
  .office b { color: var(--red); font-weight: 800; display: block; }
  .contact { left: 421px; top: 771px; font-size: 11px; font-weight: 700; line-height: 15px; }
  .contact div { display: flex; align-items: center; gap: 7px; }
  .contact .web { color: var(--red); }

  .cta-band { left: 600px; top: 762px; width: 568px; height: 93px; background: var(--red); color: #fff; }
  .cta-lead { right: 306px; top: 30px; text-align: right; font-size: 11px; line-height: 13px; font-weight: 400; letter-spacing: .6px; }
  .cta-main { left: 275px; top: 26px; font-size: 27px; font-weight: 800; letter-spacing: .5px; }
</style>
</head>
<body>

<!-- print marks -->
<div class="abs trim-box"></div>
<div class="abs fold-line" style="top:0;height:45px"></div>
<div class="abs fold-line" style="top:858px;height:42px"></div>
<div class="abs crop" style="left:42px;top:0;width:1px;height:30px"></div>
<div class="abs crop" style="left:1159px;top:0;width:1px;height:30px"></div>
<div class="abs crop" style="left:0;top:55px;width:24px;height:1px"></div>
<div class="abs crop" style="left:1176px;top:55px;width:24px;height:1px"></div>
<div class="abs crop" style="left:42px;top:870px;width:1px;height:30px"></div>
<div class="abs crop" style="left:1159px;top:870px;width:1px;height:30px"></div>
<div class="abs crop" style="left:0;top:847px;width:24px;height:1px"></div>
<div class="abs crop" style="left:1176px;top:847px;width:24px;height:1px"></div>

<!-- LEFT PANEL -->
<svg class="abs title-banner" viewBox="0 0 534 61" aria-hidden="true">
  <polygon points="0,0 506,0 534,61 0,61" fill="var(--red)"/>
</svg>
<svg class="abs title-mark" viewBox="0 0 11 11" aria-hidden="true">
  <rect x="0" y="0" width="5" height="5" fill="#fff"/>
  <rect x="6" y="0" width="5" height="5" fill="#fff"/>
  <rect x="0" y="6" width="5" height="5" fill="#fff"/>
</svg>
<div class="abs title-text"><strong style="padding-left:19px">ABOVE GROUND</strong><span>SAFE ROOMS</span></div>

<div class="abs photo" style="left:62px;top:186px;width:175px;height:158px" role="img" aria-label="White above ground safe room with closed door and lookout window"></div>
<div class="abs photo" style="left:253px;top:186px;width:125px;height:155px" role="img" aria-label="Safe room with door open showing grey interior"></div>

<p class="abs intro">Our above ground shelters are engineered, tested and meet the highest quality standards at a competitive price.  Our shelters come in a variety of sizes ranging from 3-4 people to 16-20 people. Our above ground shelters are built stronger than our competitors using a minimum of 3/16" steel, are fully painted inside and out and are made to withstand 260 mph winds. All units also come standard with a  bullet proof lookout glass window. Our safe rooms are FEMA compliant and are built using FEMA publications 320 guidelines.</p>

<h3 class="abs section-head" style="left:76px;top:375px">TYPES &amp; SIZES</h3>
<table class="abs sizes">
  <tr><th>Size</th><th>Fits</th></tr>
  <tr><td>3' × 5' or 4' × 4'</td><td>2-4 people</td></tr>
  <tr><td>4' × 6'</td><td>4-6 people</td></tr>
  <tr><td>4' × 8'</td><td>6-8 people</td></tr>
  <tr><td>5' × 7'</td><td>8-10 people</td></tr>
</table>

<h3 class="abs section-head" style="left:76px;top:501px">INSTALLATION PROCESS</h3>
<ul class="abs bullets" style="left:76px;top:514px;width:162px">
  <li>Shelter is placed with an excavator and bolted to concrete with 5/8 × 4 3/4" anchor bolts.</li>
  <li>Can be installed outside on a concrete slab of at least 15"- 20" thick.</li>
</ul>

<h3 class="abs section-head" style="left:253px;top:375px">TECHNICAL FEATURES</h3>
<ul class="abs bullets" style="left:253px;top:394px;width:154px">
  <li>3/16" steel plates for exterior skin</li>
  <li>Solid welds</li>
  <li>2" × 2" × ¼" square tubing for internal subframe</li>
  <li>3" × 3" × ¼" angle iron for bottom frame</li>
  <li>8" custom designed air vents</li>
  <li>3 BHMA/ANSI Grade 1 Dead bolt locking system</li>
  <li>Concrete anchoring system</li>
</ul>
<ul class="abs bullets" style="left:414px;top:394px;width:152px">
  <li>Bullet proof window comes standard with every shelter</li>
  <li>Double-skinned door (3/16" exterior plate and 12 gauge interior sheet</li>
  <li>3 heavy duty removable steel door hinges</li>
  <li>Door opens to the inside to keep debris from blocking door</li>
  <li>Door is removable in case of emergency</li>
</ul>

<h3 class="abs section-head" style="left:253px;top:540px">ADDITIONAL BENEFITS</h3>
<ul class="abs bullets" style="left:253px;top:552px;width:320px">
  <li>Our above ground units have a 36" side door, flat to the ground – which means they are wide enough and flat enough to be wheel chair accessible.</li>
  <li>Our above ground units are typically installed in about 2 hours.</li>
  <li>A variety of sizes to suit your need</li>
  <li>All units come standard with a bulletproof lookout glass</li>
  <li>Can also be used as a panic room</li>
</ul>

<h3 class="abs section-head" style="left:253px;top:645px">CUSTOMIZATION OPTIONS</h3>
<table class="abs custom">
  <tr><th style="width:117px">Door location</th><th style="width:97px">Door opening</th><th>Door hinges</th></tr>
  <tr>
    <td class="loc"><div>End Door (Short Side)</div><div class="alt">Side Door (Long Side Right)</div><div>Side Door (Long Side Left)</div></td>
    <td>Choice of door opening to the outside or inside of shelter</td>
    <td>Hinges can be placed on right side or left side of door</td>
  </tr>
</table>

<!-- footer -->
<div class="abs brand" style="left:74px;top:790px;font-size:14px"><i style="width:10px;height:10px"></i>STORMHAVEN</div>
<div class="abs footer-rule"></div>
<div class="abs visit">Visit our showroom at:</div>
<div class="abs office" style="left:191px;top:787px"><b>OKLAHOMA</b>4120 S. Prairie Ave.<br>Oklahoma City, OK 73150<br>(405) 555-0142</div>
<div class="abs office" style="left:297px;top:787px"><b>TULSA</b>2250 E. Ridge Ave Tulsa,<br>OK 74105 (918) 555-0187</div>
<div class="abs contact">
  <div><svg width="9" height="9" viewBox="0 0 10 10" aria-hidden="true"><path d="M2 1 L4 1 L5 3.5 L3.8 4.6 Q5 6.5 6 6.2 L7 5 L9.5 6 L9.5 8.2 Q9 9.5 7.5 9.3 Q1 8 0.7 2.5 Q0.6 1 2 1Z" fill="none" stroke="var(--ink)" stroke-width=".9"/></svg>(405) 555-0142</div>
  <div><svg width="9" height="8" viewBox="0 0 10 8" aria-hidden="true"><rect x=".5" y=".5" width="9" height="7" fill="none" stroke="var(--ink)"/><path d="M.5 .5 L5 4.5 L9.5 .5" fill="none" stroke="var(--ink)"/></svg>info@stormhaven.com</div>
  <div class="web"><svg width="9" height="9" viewBox="0 0 10 10" aria-hidden="true"><path d="M1 9 L6 4 M3 3.5 L6.5 3.5 L6.5 7" fill="none" stroke="var(--ink)" stroke-width="1"/></svg>STORMHAVEN.COM</div>
</div>

<!-- RIGHT PANEL -->
<div class="abs brand" style="left:986px;top:240px;font-size:19px"><i style="width:13px;height:13px"></i>STORMHAVEN</div>

<div class="abs" style="left:600px;top:335px;width:178px;height:417px;background:linear-gradient(180deg,#3b4148 0%,#70787f 45%,#a9b0b5 70%,#4d5257 100%)" role="img" aria-label="Tornado funnel over an empty highway under stormy sky"></div>
<div class="abs" style="left:787px;top:335px;width:381px;height:195px;background:linear-gradient(135deg,#d8d8d6,#b9bbbb 55%,#8e9293)" role="img" aria-label="Underground shelter steel hatch open in a concrete garage floor"></div>
<div class="abs" style="left:787px;top:540px;width:238px;height:212px;background:linear-gradient(180deg,#e9e4df,#d9cbbf 60%,#f2f0ee)" role="img" aria-label="Smiling family of four dressed in white"></div>
<div class="abs photo" style="left:1035px;top:540px;width:133px;height:212px" role="img" aria-label="Open white safe room door revealing interior"></div>

<div class="abs cta-band">
  <div class="abs cta-lead">BE PREPARED AND PROVIDE<br>YOUR FAMILY WITH</div>
  <div class="abs cta-main">PEACE OF MIND</div>
</div>

</body>
</html>
```